web page layout, style , color, font & flow design

We are developing a single page application. The SPA (single page application) will display natural gas pipeline flow data once the customer logs on. The customer has a choice of the region, the pipeline, the zone on the pipeline, whether the point is a delivery point or receipt point and the state the pipeline flows through.
we have jumpstarted the project and are attaching a pdf of the same.

we are using mockingbird for the wireframe. any designer is free to use this tool to make changes.

A mockingbird wireframe link is added below. you are free to use it and to make changes. please save the changed wireframe in a different name

we are looking for inputs on layout, style , color, font & flow.

A logo jpg file has also been attached.

Target Market(s)

this single web page is going to be used by natural gas traders and schedulers day in and day out. the application is more of business to business corporate application.

Industry/Entity Type

Delivery

Requirements
Must have
• layout ,flow, size, color, font , ease of use.

```html
<!DOCTYPE html>
<html lang="en">
<head>
<meta charset="utf-8">
<title>Gasline – Pipeline Flow</title>
<link href="https://fonts.googleapis.com/css2?family=Arimo:wght@400;700&display=swap" rel="stylesheet">
<style>
:root{
  --blue-dark:#0f57ae;
  --blue:#1a6cc6;
  --blue-tab:#2d88e6;
  --link:#0b5cb5;
  --text:#333;
  --muted:#777;
  --line:#dcdcdc;
  --row-alt:#e3e3e3;
  --panel-bg:#f7f7f7;
  --green:#8fd12f;
  --page:#ffffff;
}
*{box-sizing:border-box;margin:0;padding:0}
html,body{width:1200px;height:1183px;overflow:hidden;background:var(--page)}
body{font-family:"Arimo",Arial,sans-serif;color:var(--text)}
.canvas{position:relative;width:1200px;height:1183px;overflow:hidden}
.page{position:absolute;left:0;top:0;width:1420px;height:1400px;transform:scale(.84507);transform-origin:0 0;background:linear-gradient(#f6f6f6,#fff 130px);overflow:hidden}
.abs{position:absolute}
.brand{left:80px;top:40px;display:flex;align-items:center;gap:10px}
.brand-dot{width:34px;height:34px;border-radius:50%;background:var(--blue)}
.brand-name{font-size:30px;font-weight:700;color:var(--blue)}
.contact{right:76px;top:15px;font-size:11px;color:#666;display:flex;gap:16px;align-items:center}
.contact svg{vertical-align:-2px;margin-right:4px}
.user-links{right:80px;top:48px;font-size:13px;display:flex;gap:12px;align-items:center}
.user-links a{color:var(--link);text-decoration:none}
.user-links .sep{color:#ccc}
.quick-nav{left:426px;top:54px;font-size:13px;display:flex;gap:34px}
.quick-nav a{color:var(--link);text-decoration:none}
.quick-nav a.current{color:#222}
.search-box{left:416px;top:85px;width:927px;height:36px;border:1px solid var(--line);background:#fff;box-shadow:inset 0 1px 3px rgba(0,0,0,.06)}
.search-box svg{position:absolute;right:16px;top:8px}

.side{left:57px;width:339px}
.side-head{height:43px;background:linear-gradient(var(--blue),var(--blue-dark));color:#fff;font-size:15px;display:flex;align-items:center;padding:0 16px;gap:12px}
.side-head .chev{margin-left:auto}
.side-body{border:1px solid var(--line);border-top:none;background:#fff}
.sec-title{height:54px;display:flex;align-items:center;justify-content:space-between;padding:0 20px 0 15px;background:var(--panel-bg);border-bottom:1px solid #e6e6e6;color:var(--link);font-size:13px;font-weight:700}
.sec-body{border-bottom:1px solid #e6e6e6;padding:0 28px 0 15px;display:flex;align-items:center;font-size:13px;color:#555}
.select{border:1px solid #d6d6d6;height:31px;display:flex;align-items:center;background:#fff;font-size:13px;color:#555}
.select span{flex:1;padding-left:11px}
.select i{width:31px;height:100%;border-left:1px solid #d6d6d6;display:flex;align-items:center;justify-content:center}
.check{display:flex;align-items:center;gap:8px;margin-right:34px}
.check b{width:19px;height:19px;border:1px solid #ccc;background:#fff;display:block}
.btn-search{display:block;margin:0 auto;width:191px;height:25px;background:linear-gradient(#9ddb3c,#7fc41f);color:#fff;font-weight:700;font-size:14px;text-align:center;line-height:25px}
.pipe-item{height:54px;display:flex;align-items:center;justify-content:space-between;padding:0 20px 0 15px;background:var(--panel-bg);border-bottom:1px solid #e3e3e3;color:var(--link);font-size:13px;font-weight:700}

.regions{left:416px;top:143px;display:flex;gap:8px}
.regions div{width:133px;height:43px;background:var(--blue-tab);color:#fff;font-size:15px;display:flex;align-items:center;justify-content:center}
.regions div.active{background:var(--blue-dark)}
.results{left:416px;top:186px;width:927px;height:889px;border:1px solid var(--line);background:#fff}
.sort-title{position:absolute;left:23px;top:29px;font-size:13px;color:#222}
.rule{position:absolute;left:15px;right:15px;height:1px;background:var(--line)}
.filters{position:absolute;left:25px;top:80px;display:flex;align-items:center;font-size:13px;color:#555}
.filters .select{margin-left:10px}
table{position:absolute;left:15px;top:165px;width:894px;border-collapse:separate;border-spacing:0;font-size:12.5px}
th{height:35px;font-weight:400;color:#555;border:1px solid var(--line);border-right:none;background:#fff}
th:last-child{border-right:1px solid var(--line)}
th:first-child{text-align:left;padding-left:12px}
.gap td{height:10px;border:none}
td{height:34.8px;text-align:center;color:#888;border-left:1px solid var(--line);border-bottom:1px solid #eee}
td:last-child{border-right:1px solid var(--line)}
tbody tr:nth-child(odd) td{background:var(--row-alt)}
tbody tr.gap td{background:none}
tbody tr.first td{background:#fff}
.pager{position:absolute;right:27px;top:852px;font-size:13px;display:flex;gap:14px;color:#bbb}
.pager a{color:var(--link);text-decoration:none}
</style>
</head>
<body>
<div class="canvas">
<div class="page">
  <div class="abs brand"><span class="brand-dot"></span><span class="brand-name">Gasline</span></div>

  <div class="abs contact">
    <span><svg width="12" height="10" viewBox="0 0 12 10"><rect x=".5" y=".5" width="11" height="9" fill="none" stroke="#888"/><path d="M3 3h6M3 5h6M3 7h6" stroke="#888"/></svg>48 Meridian Avenue, 2nd Floor, Riverton, Ohio 44010</span>
    <span><svg width="7" height="11" viewBox="0 0 7 11"><rect x=".5" y=".5" width="6" height="10" rx="1" fill="none" stroke="#888"/></svg>(555) 014-2290</span>
  </div>
  <div class="abs user-links">
    <svg width="12" height="12" viewBox="0 0 12 12"><circle cx="6" cy="6" r="6" fill="#7cc22a"/><text x="6" y="9.5" font-size="9" fill="#fff" text-anchor="middle" font-family="Arial">?</text></svg>
    <a href="#">Help</a><span class="sep">|</span><a href="#">Logout</a><span class="sep">|</span>
    <svg width="11" height="12" viewBox="0 0 11 12"><circle cx="5.5" cy="3.5" r="3" fill="#7cc22a"/><path d="M0 12c0-4 11-4 11 0z" fill="#7cc22a"/></svg>
    <a href="#">Dana</a>
  </div>
  <nav class="abs quick-nav"><a class="current" href="#">Quick Search</a><a href="#">State</a><a href="#">Other</a></nav>
  <div class="abs search-box"><svg width="20" height="20" viewBox="0 0 20 20"><circle cx="8" cy="8" r="7" fill="none" stroke="#ddd" stroke-width="2"/><path d="M13 13l6 6" stroke="#ddd" stroke-width="2"/></svg></div>

  <aside class="abs side" style="top:145px">
    <div class="side-head"><svg width="20" height="14" viewBox="0 0 20 14"><path d="M1 9h18v4H1zM8 3h4v6H8zM5 1h10v2H5z" fill="#fff"/></svg>Search Preferences<svg class="chev" width="18" height="10" viewBox="0 0 18 10"><path d="M1 1l8 8 8-8" fill="none" stroke="#fff" stroke-width="1.5"/></svg></div>
    <div class="side-body">
      <div class="sec-title">Pipeline Region<svg width="14" height="14"><circle cx="7" cy="7" r="7" fill="#aaa"/><path d="M3.5 7h7" stroke="#fff" stroke-width="2"/></svg></div>
      <div class="sec-body" style="height:94px">Region:<div class="select" style="margin-left:32px;width:218px"><span>Choose &nbsp;Region</span><i><svg width="11" height="8"><path d="M0 0h11L5.5 8z" fill="var(--link)"/></svg></i></div></div>
      <div class="sec-title">Pipeline Zone<svg width="14" height="14"><circle cx="7" cy="7" r="7" fill="#aaa"/><path d="M3.5 7h7" stroke="#fff" stroke-width="2"/></svg></div>
      <div class="sec-body" style="height:95px">Zone:<div class="select" style="margin-left:58px;width:218px"><span>Choose &nbsp;Zone</span><i><svg width="11" height="8"><path d="M0 0h11L5.5 8z" fill="var(--link)"/></svg></i></div></div>
      <div class="sec-title">Pipeline Type<svg width="14" height="14"><circle cx="7" cy="7" r="7" fill="#aaa"/><path d="M3.5 7h7" stroke="#fff" stroke-width="2"/></svg></div>
      <div class="sec-body" style="height:81px;padding-left:24px"><label class="check"><b></b>Delivery Point</label><label class="check"><b></b>Receipt Point</label></div>
      <div class="sec-title">State of the Pipeline<svg width="14" height="14"><circle cx="7" cy="7" r="7" fill="#aaa"/><path d="M3.5 7h7" stroke="#fff" stroke-width="2"/></svg></div>
      <div style="height:146px;padding:27px 22px 0 21px">
        <div style="display:flex;align-items:center;font-size:13px;color:#555;line-height:15px"><span style="width:76px">State of the Pipeline:</span><div class="select" style="width:218px"><span>Available</span><i><svg width="11" height="8"><path d="M0 0h11L5.5 8z" fill="var(--link)"/></svg></i></div></div>
        <div class="btn-search" style="margin-top:35px">Search</div>
      </div>
    </div>
  </aside>

  <aside class="abs side" style="top:845px">
    <div class="side-head"><svg width="20" height="14" viewBox="0 0 20 14"><path d="M1 9h18v4H1zM8 3h4v6H8zM5 1h10v2H5z" fill="#fff"/></svg>Pipelines<svg class="chev" width="18" height="10" viewBox="0 0 18 10"><path d="M1 1l8 8 8-8" fill="none" stroke="#fff" stroke-width="1.5"/></svg></div>
    <div class="side-body">
      <div class="pipe-item">Alderbrook<svg width="14" height="14"><circle cx="7" cy="7" r="7" fill="#aaa"/><path d="M3.5 7h7M7 3.5v7" stroke="#fff" stroke-width="2"/></svg></div>
      <div class="pipe-item">CVT<svg width="14" height="14"><circle cx="7" cy="7" r="7" fill="#aaa"/><path d="M3.5 7h7M7 3.5v7" stroke="#fff" stroke-width="2"/></svg></div>
      <div class="pipe-item">Dunmore<svg width="14" height="14"><circle cx="7" cy="7" r="7" fill="#aaa"/><path d="M3.5 7h7M7 3.5v7" stroke="#fff" stroke-width="2"/></svg></div>
      <div class="pipe-item">Western Shore NG<svg width="14" height="14"><circle cx="7" cy="7" r="7" fill="#aaa"/><path d="M3.5 7h7M7 3.5v7" stroke="#fff" stroke-width="2"/></svg></div>
      <div class="pipe-item">West Tallow NG<svg width="14" height="14"><circle cx="7" cy="7" r="7" fill="#aaa"/><path d="M3.5 7h7M7 3.5v7" stroke="#fff" stroke-width="2"/></svg></div>
      <div class="pipe-item">Ember Gas<svg width="14" height="14"><circle cx="7" cy="7" r="7" fill="#aaa"/><path d="M3.5 7h7M7 3.5v7" stroke="#fff" stroke-width="2"/></svg></div>
      <div class="pipe-item">Equiline Inc<svg width="14" height="14"><circle cx="7" cy="7" r="7" fill="#aaa"/><path d="M3.5 7h7M7 3.5v7" stroke="#fff" stroke-width="2"/></svg></div>
      <div class="pipe-item">Slate Ridge Gas<svg width="14" height="14"><circle cx="7" cy="7" r="7" fill="#aaa"/><path d="M3.5 7h7M7 3.5v7" stroke="#fff" stroke-width="2"/></svg></div>
      <div class="pipe-item">Ironwood<svg width="14" height="14"><circle cx="7" cy="7" r="7" fill="#aaa"/><path d="M3.5 7h7M7 3.5v7" stroke="#fff" stroke-width="2"/></svg></div>
      <div class="pipe-item">Mariner &amp; Northway<svg width="14" height="14"><circle cx="7" cy="7" r="7" fill="#aaa"/><path d="M3.5 7h7M7 3.5v7" stroke="#fff" stroke-width="2"/></svg></div>
    </div>
  </aside>

  <div class="abs regions"><div class="active">NorthEast</div><div>MidWest</div><div>SouthEast</div><div>SouthWest</div><div>Central</div><div>West</div></div>

  <section class="abs results">
    <div class="sort-title">Sort Results by:</div>
    <div class="rule" style="top:56px"></div>
    <div class="filters">
      Location Type:<div class="select" style="width:172px;margin-right:24px"><span>All</span><i><svg width="11" height="8"><path d="M0 0h11L5.5 8z" fill="var(--link)"/></svg></i></div>
      Interstate pipeline<div class="select" style="width:172px;margin-right:32px;margin-left:7px"><span>All</span><i><svg width="11" height="8"><path d="M0 0h11L5.5 8z" fill="var(--link)"/></svg></i></div>
      Pipeline zones:<div class="select" style="width:172px;margin-left:7px;position:relative;top:2px"><span>Zones</span><i><svg width="11" height="8"><path d="M0 0h11L5.5 8z" fill="var(--link)"/></svg></i></div>
    </div>
    <div class="rule" style="top:136px"></div>
    <table>
      <colgroup><col style="width:87px"><col style="width:107px"><col style="width:109px"><col style="width:115px"><col style="width:120px"><col style="width:103px"><col style="width:108px"><col style="width:145px"></colgroup>
      <thead><tr><th>gasday</th><th>location</th><th>loc_Name</th><th>Flow_Ind</th><th>L oc_Desc</th><th>Op_cap</th><th>Sch_cap</th><th>Op_avail_cap</th></tr></thead>
      <tbody>
        <tr class="gap"><td colspan="8"></td></tr>
        <tr class="first"><td>Item 1</td><td>Item 2</td><td>Item 3</td><td>Item 4</td><td>Item 5</td><td>Item 6</td><td>Item 7</td><td>Item 8</td></tr>
        <tr><td>Item 1</td><td>Item 2</td><td>Item 3</td><td>Item 4</td><td>Item 5</td><td>Item 6</td><td>Item 7</td><td>Item 8</td></tr>
        <tr><td>Item 1</td><td>Item 2</td><td>Item 3</td><td>Item 4</td><td>Item 5</td><td>Item 6</td><td>Item 7</td><td>Item 8</td></tr>
        <tr><td>Item 1</td><td>Item 2</td><td>Item 3</td><td>Item 4</td><td>Item 5</td><td>Item 6</td><td>Item 7</td><td>Item 8</td></tr>
        <tr><td>Item 1</td><td>Item 2</td><td>Item 3</td><td>Item 4</td><td>Item 5</td><td>Item 6</td><td>Item 7</td><td>Item 8</td></tr>
        <tr><td>Item 1</td><td>Item 2</td><td>Item 3</td><td>Item 4</td><td>Item 5</td><td>Item 6</td><td>Item 7</td><td>Item 8</td></tr>
        <tr><td>Item 1</td><td>Item 2</td><td>Item 3</td><td>Item 4</td><td>Item 5</td><td>Item 6</td><td>Item 7</td><td>Item 8</td></tr>
        <tr><td>Item 1</td><td>Item 2</td><td>Item 3</td><td>Item 4</td><td>Item 5</td><td>Item 6</td><td>Item 7</td><td>Item 8</td></tr>
        <tr><td>Item 1</td><td>Item 2</td><td>Item 3</td><td>Item 4</td><td>Item 5</td><td>Item 6</td><td>Item 7</td><td>Item 8</td></tr>
        <tr><td>Item 1</td><td>Item 2</td><td>Item 3</td><td>Item 4</td><td>Item 5</td><td>Item 6</td><td>Item 7</td><td>Item 8</td></tr>
        <tr><td>Item 1</td><td>Item 2</td><td>Item 3</td><td>Item 4</td><td>Item 5</td><td>Item 6</td><td>Item 7</td><td>Item 8</td></tr>
        <tr><td>Item 1</td><td>Item 2</td><td>Item 3</td><td>Item 4</td><td>Item 5</td><td>Item 6</td><td>Item 7</td><td>Item 8</td></tr>
        <tr><td>Item 1</td><td>Item 2</td><td>Item 3</td><td>Item 4</td><td>Item 5</td><td>Item 6</td><td>Item 7</td><td>Item 8</td></tr>
        <tr><td>Item 1</td><td>Item 2</td><td>Item 3</td><td>Item 4</td><td>Item 5</td><td>Item 6</td><td>Item 7</td><td>Item 8</td></tr>
        <tr><td>Item 1</td><td>Item 2</td><td>Item 3</td><td>Item 4</td><td>Item 5</td><td>Item 6</td><td>Item 7</td><td>Item 8</td></tr>
        <tr><td>Item 1</td><td>Item 2</td><td>Item 3</td><td>Item 4</td><td>Item 5</td><td>Item 6</td><td>Item 7</td><td>Item 8</td></tr>
        <tr><td>Item 1</td><td>Item 2</td><td>Item 3</td><td>Item 4</td><td>Item 5</td><td>Item 6</td><td>Item 7</td><td>Item 8</td></tr>
        <tr><td>Item 1</td><td>Item 2</td><td>Item 3</td><td>Item 4</td><td>Item 5</td><td>Item 6</td><td>Item 7</td><td>Item 8</td></tr>
      </tbody>
    </table>
    <div class="pager"><span>1</span><a href="#">2</a><a href="#">&gt;</a></div>
  </section>
</div>
</div>
</body>
</html>
```